New Jazz Music Album CD Design

Need a contemporary jazz CD cover for my single I will be releasing December 31. Name of the song is called Velvet Drift . Artist Name is Dorian Mapes. Website is Http://DorianM.com. Please find a way to incorporate my attached logo and add my attached picture somewhere to the album art. Front Cover Demensions width 1423 pixel height 1411 pixels RGB 16 color no bleed. Inside Front Cover Demensions width 1423 pixel height 1411 pixels RGB 16 color no bleed. Disc dimensions Diameter: 1394 pixels RGB 16 bit color. Back tray card with 2 spines width (includes 2 spines) 1772 pixels height 1385 pixels spine width 74 pixels.
Updates

The images in the path below will also suffice for the design https://qkfiles.example/f/s!BtRZLMWc7WHMjoTt6ZI65SbxyQ4a

Target Market(s)

Age group 35 and older. Smooth jazz listeners.

Industry/Entity Type

Music Download

Font styles to use
Serif
Sans Serif

Colors

Designer to choose colors to be used in the design.

Requirements
Must have
• Song title Velvet Drift
• Artist name: Dorian M
• Attached Logo
• Website: DorianM.com
Nice to have
• NA
Should not have
• Na

```html
<!DOCTYPE html>
<html lang="en">
<head>
<meta charset="utf-8">
<title>Dorian M – Velvet Drift</title>
<link rel="stylesheet" href="https://fonts.googleapis.com/css2?family=Abril+Fatface&family=Playfair+Display:wght@900&family=Montserrat:wght@500&display=swap">
<style>
  :root {
    --ink: #0b0806;
    --white: #ffffff;
    --artist-red: #c8141c;
    --logo-grey: #8d8f92;
    --logo-text: #2a2a2c;
    --warm-light: #b9873f;
    --warm-mid: #5a3d27;
    --warm-dark: #1e1511;
    --skin: #6b4330;
    --jacket: #4a1d34;
    --shirt: #1f2a3a;
  }
  * { margin: 0; padding: 0; box-sizing: border-box; }
  html, body { width: 1200px; height: 1200px; overflow: hidden; background: var(--ink); }
  .cover { position: relative; width: 1200px; height: 1200px; overflow: hidden; }
  .lounge-backdrop { position: absolute; inset: 0; width: 100%; height: 100%; }
  .artist-portrait { position: absolute; left: 470px; top: 60px; width: 730px; height: 1140px; }
  .logo-panel {
    position: absolute; left: 70px; top: 66px; width: 333px; height: 192px;
    background: linear-gradient(180deg, #a3a5a8, var(--logo-grey));
    display: flex; align-items: center; justify-content: center;
  }
  .logo-name {
    font-family: "Playfair Display", serif; font-weight: 900;
    font-size: 50px; color: var(--logo-text); letter-spacing: 1px;
  }
  .artist-name {
    position: absolute; left: 71px; top: 658px;
    font-family: "Playfair Display", serif; font-weight: 900;
    font-size: 72px; color: var(--artist-red); letter-spacing: -1px; line-height: 1;
  }
  .song-title {
    position: absolute; left: 66px; top: 770px;
    font-family: "Abril Fatface", serif; font-size: 200px; line-height: 0.93;
    color: var(--white); letter-spacing: -6px;
    text-shadow: 0 0 2px var(--ink), 3px 3px 0 var(--ink), -2px -2px 0 var(--ink), 3px -2px 0 var(--ink), -2px 3px 0 var(--ink);
  }
  .song-title span { display: block; }
  .website {
    position: absolute; left: 905px; top: 1100px;
    font-family: "Montserrat", sans-serif; font-weight: 500;
    font-size: 38px; color: var(--white); letter-spacing: -0.5px;
  }
</style>
</head>
<body>
  <main class="cover">
    <svg class="lounge-backdrop" viewBox="0 0 1200 1200" role="img" aria-label="Warmly lit lounge interior with hanging lamps, softly out of focus">
      <defs>
        <linearGradient id="room" x1="0" y1="0" x2="1" y2="1">
          <stop offset="0" stop-color="var(--warm-mid)"/>
          <stop offset="0.5" stop-color="var(--warm-dark)"/>
          <stop offset="1" stop-color="#120c0a"/>
        </linearGradient>
        <radialGradient id="glow" cx="0.3" cy="0.1" r="0.55">
          <stop offset="0" stop-color="var(--warm-light)" stop-opacity="0.7"/>
          <stop offset="1" stop-color="var(--warm-light)" stop-opacity="0"/>
        </radialGradient>
      </defs>
      <rect width="1200" height="1200" fill="url(#room)"/>
      <rect width="1200" height="1200" fill="url(#glow)"/>
    </svg>

    <svg class="artist-portrait" viewBox="0 0 730 1140" role="img" aria-label="Portrait of the artist smiling, wearing a plum jacket and dark shirt, holding a saxophone">
      <defs>
        <linearGradient id="portrait" x1="0" y1="0" x2="0" y2="1">
          <stop offset="0" stop-color="var(--skin)" stop-opacity="0"/>
          <stop offset="0.08" stop-color="var(--skin)"/>
          <stop offset="0.52" stop-color="var(--skin)"/>
          <stop offset="0.62" stop-color="var(--shirt)"/>
          <stop offset="0.75" stop-color="var(--jacket)"/>
          <stop offset="1" stop-color="var(--jacket)"/>
        </linearGradient>
        <linearGradient id="fadeLeft" x1="0" y1="0" x2="1" y2="0">
          <stop offset="0" stop-color="#fff" stop-opacity="0"/>
          <stop offset="0.18" stop-color="#fff" stop-opacity="1"/>
          <stop offset="1" stop-color="#fff" stop-opacity="1"/>
        </linearGradient>
        <mask id="portraitMask"><rect width="730" height="1140" fill="url(#fadeLeft)"/></mask>
      </defs>
      <rect width="730" height="1140" fill="url(#portrait)" mask="url(#portraitMask)"/>
    </svg>

    <div class="logo-panel"><span class="logo-name">DORIAN M.</span></div>

    <h2 class="artist-name">DORIAN M</h2>
    <h1 class="song-title"><span>Velvet</span><span>Drift</span></h1>
    <p class="website">DorianM.com</p>
  </main>
</body>
</html>
```